Heron Ridge Distillery Bottle Label Design

We need a label design for a product called "Cedar Hollow Straight Bourbon Whiskey". The bottle has two embossments on the side and an image printed on the back that will show through when looking from the front (shown in the attached image). It's made of 30% rye and 70% corn; images of the ingredients can be incorporated into the label design. We are a distillery that produces whiskey and bourbon from local farmers around the area. We focus on the quality of the ingredients and using the recipes passed down from generation to generation. We like a straight forward design using two colors maximum. The background will be brown once filled with the bourbon, so it must contrast against it (i.e. white and other lighter colors). The Heron Ridge Distillery logo must be present on the bottle front, as well as 750 ml, 84 PROOF, 42% ALC/VOL.

Target Market(s)

Craft whiskey consumers.

Industry/Entity Type

Product

Colors
fee18a
fbe7d2
fff3d1
fefcee
fefdec
fdf9cf

Requirements
Must have
• 750 ml, 84 PROOF, 42% ALC/VOL. Aged for 3 years.The Heron Ridge Distillery logo must be present on the bottle. Only two colors on label.
Nice to have
• Story of how we are a micro distillery making hand crafted whiskey.
Should not have
• False or misleading print.

```html
<!DOCTYPE html>
<html lang="en">
<head>
<meta charset="utf-8">
<title>Heron Ridge Distillery – Cedar Hollow Label</title>
<link rel="stylesheet" href="https://fonts.googleapis.com/css2?family=Oswald:wght@400;600&display=swap">
<style>
  :root {
    --paper: #ffffff;
    --espresso: #221a17;
    --wheat: #e3cda4;
  }
  html, body {
    margin: 0;
    padding: 0;
    overflow: hidden;
  }
  .canvas {
    position: relative;
    width: 1200px;
    height: 1000px;
    background: var(--paper);
    overflow: hidden;
  }
  .label {
    position: absolute;
    top: 98px;
    width: 357px;
    height: 477px;
  }
  .label--dark  { left: 98px;  --ground: var(--espresso); --ink: var(--wheat); }
  .label--light { left: 488px; --ground: var(--wheat);    --ink: var(--espresso); }

  .label__ground { fill: var(--ground); }
  .label__rule   { fill: none; stroke: var(--ink); stroke-width: 1.6; }
  .label__seal   { fill: var(--ground); stroke: var(--ink); stroke-width: 2; }
  .label__text   { fill: var(--ink); font-family: "Oswald", sans-serif; }

  .brand-name     { font-size: 28px; font-weight: 600; letter-spacing: 1px; }
  .brand-sub      { font-size: 14px; font-weight: 600; letter-spacing: 4px; }
  .product-name   { font-size: 40px; font-weight: 600; }
  .product-style  { font-size: 11px; font-weight: 600; letter-spacing: 1.2px; }
  .volume         { font-size: 19px; font-weight: 600; letter-spacing: 1px; }
  .strength       { font-size: 10px; font-weight: 400; letter-spacing: 0.5px; }
</style>
</head>
<body>
<main class="canvas">

  <svg class="label label--dark" viewBox="0 0 357 477" role="img" aria-label="Cedar Hollow bourbon label, dark version">
    <rect class="label__ground" width="357" height="477"/>
    <path class="label__rule" d="M51 40 H306 A14 14 0 0 0 320 54 V433 A14 14 0 0 0 306 447 H51 A14 14 0 0 0 37 433 V54 A14 14 0 0 0 51 40 Z"/>
    <path class="label__rule" d="M54 45 H303 A12 12 0 0 0 315 57 V430 A12 12 0 0 0 303 442 H54 A12 12 0 0 0 42 430 V57 A12 12 0 0 0 54 45 Z"/>
    <line class="label__rule" x1="42" y1="57" x2="315" y2="57"/>
    <line class="label__rule" x1="42" y1="80" x2="315" y2="80"/>
    <circle class="label__seal" cx="178" cy="92" r="40"/>
    <text class="label__text brand-name" x="178" y="172" text-anchor="middle">HERON RIDGE</text>
    <text class="label__text brand-sub" x="180" y="196" text-anchor="middle">DISTILLERY</text>
    <line class="label__rule" x1="116" y1="205" x2="242" y2="205"/>
    <text class="label__text product-name" x="178" y="298" text-anchor="middle" textLength="238" lengthAdjust="spacingAndGlyphs">CEDAR HOLLOW</text>
    <text class="label__text product-style" x="178" y="315" text-anchor="middle">STRAIGHT BOURBON WHISKEY</text>
    <line class="label__rule" x1="42" y1="352" x2="315" y2="352"/>
    <text class="label__text volume" x="178" y="386" text-anchor="middle">750 ml</text>
    <text class="label__text strength" x="72" y="424">84 PROOF</text>
    <text class="label__text strength" x="287" y="424" text-anchor="end">42% ALC/VOL</text>
  </svg>

  <svg class="label label--light" viewBox="0 0 357 477" role="img" aria-label="Cedar Hollow bourbon label, light version">
    <rect class="label__ground" width="357" height="477"/>
    <path class="label__rule" d="M51 40 H306 A14 14 0 0 0 320 54 V433 A14 14 0 0 0 306 447 H51 A14 14 0 0 0 37 433 V54 A14 14 0 0 0 51 40 Z"/>
    <path class="label__rule" d="M54 45 H303 A12 12 0 0 0 315 57 V430 A12 12 0 0 0 303 442 H54 A12 12 0 0 0 42 430 V57 A12 12 0 0 0 54 45 Z"/>
    <line class="label__rule" x1="42" y1="57" x2="315" y2="57"/>
    <line class="label__rule" x1="42" y1="80" x2="315" y2="80"/>
    <circle class="label__seal" cx="178" cy="92" r="40"/>
    <text class="label__text brand-name" x="178" y="172" text-anchor="middle">HERON RIDGE</text>
    <text class="label__text brand-sub" x="180" y="196" text-anchor="middle">DISTILLERY</text>
    <line class="label__rule" x1="116" y1="205" x2="242" y2="205"/>
    <text class="label__text product-name" x="178" y="298" text-anchor="middle" textLength="238" lengthAdjust="spacingAndGlyphs">CEDAR HOLLOW</text>
    <text class="label__text product-style" x="178" y="315" text-anchor="middle">STRAIGHT BOURBON WHISKEY</text>
    <line class="label__rule" x1="42" y1="352" x2="315" y2="352"/>
    <text class="label__text volume" x="178" y="386" text-anchor="middle">750 ml</text>
    <text class="label__text strength" x="72" y="424">84 PROOF</text>
    <text class="label__text strength" x="287" y="424" text-anchor="end">42% ALC/VOL</text>
  </svg>

</main>
</body>
</html>
```